Business Card / Appointment Card for Physician

On one side it should give the logo, address, and contact information, and on the other side it should br an Appointment card.

One Side:
Logo (see attached files)
Board Certified American Orthopedic Surgery

1487 Harrowgate Ave.
Suite KM7
Bronx, NY 10527
Tel: (718) 552 - 1948
Fax: (718) 552 - 7210

628 Fourth Ave.
Suite 42
New York, NY 10087
Tel: (212) 734 - 2815

Second Side:
Appointment
give them a choice of Bronx or Mahattan office
For:
Date:
Time:

If you are unable to keep your appointment, please call (718) 263-5102 24hrs in advance.

Target Market(s)

People that need orthopedic surgery

Industry/Entity Type

Business

Contact Information for Business Card

smart and attractive

Requirements
Must have
• logo
• contact information on one side, appointment information on the other

```html
<!DOCTYPE html>
<html lang="en">
<head>
<meta charset="utf-8">
<title>David R. Halloran MD PC – Business Card</title>
<link rel="stylesheet" href="https://fonts.googleapis.com/css2?family=Raleway:wght@400;500;600;700&display=swap">
<style>
  :root {
    --brand-blue: #1f66b2;
    --text-blue: #2b6cb6;
    --accent-green: #5ccc2a;
    --tint-cyan: #e3f8fb;
    --tint-green: #eef9e6;
    --tint-blue: #e9eef6;
    --paper: #ffffff;
  }
  * { box-sizing: border-box; margin: 0; padding: 0; }
  html, body {
    width: 1200px; height: 700px; overflow: hidden;
    background: var(--paper);
    font-family: "Raleway", sans-serif;
  }
  .card {
    position: relative; width: 1200px; height: 700px;
    overflow: hidden; background: var(--paper);
  }
  .backdrop { position: absolute; }
  .backdrop--left {
    left: -60px; top: -20px; width: 540px; height: 760px;
    border-radius: 0 320px 0 0;
    background: linear-gradient(180deg, var(--tint-cyan) 0%, rgba(227,248,251,0.35) 70%, var(--tint-blue) 100%);
    opacity: 0.8;
  }
  .backdrop--right {
    right: -80px; top: 20px; width: 560px; height: 720px;
    border-radius: 320px 0 0 0;
    background: linear-gradient(200deg, var(--tint-green) 0%, rgba(238,249,230,0.5) 80%);
  }
  .brand {
    position: absolute; left: 0; right: 0; top: 82px;
    text-align: center; color: var(--brand-blue);
  }
  .brand__mark {
    width: 156px; height: 156px; margin: 0 auto;
    border-radius: 50%; background: var(--brand-blue);
  }
  .brand__name {
    margin-top: 10px;
    font-size: 48px; font-weight: 600; letter-spacing: 0; line-height: 1;
  }
  .brand__tagline {
    margin-top: 8px;
    font-size: 25px; font-weight: 700; letter-spacing: 0.2px; line-height: 1;
  }
  .credential-band {
    position: absolute; left: 0; top: 352px; width: 1200px; height: 71px;
    background: var(--brand-blue); color: #fff;
    display: flex; align-items: center; justify-content: center;
    font-size: 29px; font-weight: 500; letter-spacing: 2px;
  }
  .office {
    position: absolute; top: 442px;
    color: var(--text-blue); font-size: 29px; font-weight: 400;
    line-height: 37px; list-style: none;
  }
  .office--bronx { left: 160px; }
  .office--manhattan { left: 710px; }
  .office__line { display: flex; align-items: center; height: 37px; }
  .office__line--indent { padding-left: 34px; }
  .office__icon { width: 26px; height: 26px; margin-right: 8px; flex: none; }
</style>
</head>
<body>
<main class="card">
  <div class="backdrop backdrop--left" role="img" aria-label="Faint knee joint line drawing in soft cyan"></div>
  <div class="backdrop backdrop--right" role="img" aria-label="Faint shoulder joint line drawing in soft green"></div>

  <header class="brand">
    <div class="brand__mark"></div>
    <h1 class="brand__name">DAVID R. HALLORAN MD PC</h1>
    <p class="brand__tagline">ORTHOPAEDIC SURGERY &amp; SPORTS MEDICINE</p>
  </header>

  <div class="credential-band">BOARD CERTIFIED AMERICAN ORTHOPEDIC SURGERY</div>

  <ul class="office office--bronx">
    <li class="office__line">
      <svg class="office__icon" viewBox="0 0 24 24"><path fill="var(--accent-green)" d="M12 1.5a7.5 7.5 0 0 0-7.5 7.5c0 5.4 7.5 13.5 7.5 13.5s7.5-8.1 7.5-13.5A7.5 7.5 0 0 0 12 1.5z"/><circle cx="12" cy="9" r="3" fill="#fff"/></svg>
      1487 Harrowgate Ave.</li>
    <li class="office__line office__line--indent">Suite KM7</li>
    <li class="office__line office__line--indent">Bronx, NY 10527</li>
    <li class="office__line">
      <svg class="office__icon" viewBox="0 0 24 24"><circle cx="12" cy="12" r="12" fill="var(--accent-green)"/><path fill="#fff" d="M8.2 5.5l2 3.2-1.3 1.5c.9 1.9 2.3 3.3 4.2 4.2l1.5-1.3 3.2 2-1 2.6c-5.6.1-10.7-5-10.6-10.6z"/></svg>
      Tel (718) 552 - 1948</li>
    <li class="office__line">
      <svg class="office__icon" viewBox="0 0 24 24"><circle cx="12" cy="12" r="12" fill="var(--accent-green)"/><rect x="8" y="5.5" width="8" height="4" fill="#fff"/><rect x="5.5" y="10" width="13" height="6" rx="1" fill="#fff"/><rect x="8" y="14" width="8" height="4.5" fill="#fff" stroke="var(--accent-green)" stroke-width="1"/></svg>
      Fax (718) 552 - 7210</li>
  </ul>

  <ul class="office office--manhattan">
    <li class="office__line">
      <svg class="office__icon" viewBox="0 0 24 24"><path fill="var(--accent-green)" d="M12 1.5a7.5 7.5 0 0 0-7.5 7.5c0 5.4 7.5 13.5 7.5 13.5s7.5-8.1 7.5-13.5A7.5 7.5 0 0 0 12 1.5z"/><circle cx="12" cy="9" r="3" fill="#fff"/></svg>
      628 Fourth Ave.</li>
    <li class="office__line office__line--indent">Suite 42</li>
    <li class="office__line office__line--indent">New York, NY 10087</li>
    <li class="office__line">
      <svg class="office__icon" viewBox="0 0 24 24"><circle cx="12" cy="12" r="12" fill="var(--accent-green)"/><path fill="#fff" d="M8.2 5.5l2 3.2-1.3 1.5c.9 1.9 2.3 3.3 4.2 4.2l1.5-1.3 3.2 2-1 2.6c-5.6.1-10.7-5-10.6-10.6z"/></svg>
      Tel (212) 734 - 2815</li>
  </ul>
</main>
</body>
</html>
```